Orvella Aid Fund - New Website Design

I need a site that looks like this http://renwick-gives-now.org for boat donations. So please replace the cars with boats.

```html
<!DOCTYPE html>
<html lang="en">
<head>
<meta charset="utf-8">
<title>Orvella Aid Fund – Donate Boat to Charity</title>
<link href="https://fonts.googleapis.com/css2?family=Roboto:wght@300;400;500;700&display=swap" rel="stylesheet">
<style>
:root{
  --teal:#3fc1cf;
  --teal-dark:#2aa9b8;
  --green:#8cc63f;
  --pink:#f07a8c;
  --ink:#333640;
  --muted:#8a8e96;
  --line:#e3e5e8;
  --grey-bg:#f5f5f6;
  --footer:#2e323d;
  --footer-deep:#262a33;
  --white:#ffffff;
}
*{box-sizing:border-box;margin:0;padding:0}
html,body{width:1200px;height:2448px;overflow:hidden}
body{font-family:"Roboto",Arial,sans-serif;color:var(--ink);background:var(--white);position:relative}
.abs{position:absolute}

/* header */
.site-header{position:absolute;left:0;top:0;width:1200px;height:62px;background:var(--white);border-bottom:1px solid var(--line)}
.brand{position:absolute;left:30px;top:17px;font-size:22px;font-weight:400;color:var(--ink);letter-spacing:.2px}
.main-nav{position:absolute;left:284px;top:0;display:flex;height:62px}
.main-nav a{display:block;padding:24px 14px 0;font-size:12px;color:var(--ink);text-decoration:none;font-weight:500}
.main-nav a.active{border-top:3px solid var(--teal);padding-top:21px;color:var(--teal)}
.call{position:absolute;left:850px;top:15px;display:flex;align-items:center;gap:10px}
.call-text{font-size:10px;color:var(--muted);line-height:1.3}
.call-text strong{display:block;color:var(--ink);font-size:12px;font-weight:500}
.btn-green{position:absolute;left:1000px;top:17px;width:96px;height:30px;background:var(--green);color:#fff;font-size:12px;font-weight:500;display:flex;align-items:center;justify-content:center;border-radius:2px}

/* hero */
.hero{position:absolute;left:0;top:62px;width:1200px;height:548px;background:linear-gradient(100deg,#6f8796 0%,#9bb0bd 35%,#c6d1d6 60%,#aab8be 100%)}
.hero-shade{position:absolute;inset:0;background:linear-gradient(180deg,rgba(0,0,0,0) 55%,rgba(60,50,40,.35) 100%)}
.hero-title{position:absolute;left:42px;top:212px;color:#fff;font-weight:300;line-height:1.05}
.hero-title .s1{font-size:36px;display:block}
.hero-title .s2{font-size:58px;display:block}
.hero-sub{position:absolute;left:42px;top:320px;color:#fff;font-size:20px;font-weight:300}

/* form */
.pickup-form{position:absolute;left:772px;top:142px;width:336px;height:560px;background:#fff;box-shadow:0 6px 24px rgba(0,0,0,.18);padding:22px 24px}
.pickup-form h3{font-size:17px;font-weight:400;color:var(--ink);padding-bottom:16px;border-bottom:1px solid var(--line)}
.form-label{font-size:9px;font-weight:700;letter-spacing:.6px;color:var(--ink);margin:18px 0 12px}
.row{display:flex;gap:14px;margin-bottom:12px}
.field{flex:1;height:34px;border:1px solid var(--line);font-size:10px;color:#a3a7ad;padding:11px 10px;position:relative}
.field.select::after{content:"";position:absolute;right:10px;top:14px;border:4px solid transparent;border-top-color:#888}
.form-sep{border-top:1px solid var(--line);margin-top:22px}
.btn-outline{display:inline-flex;align-items:center;gap:8px;height:30px;padding:0 14px;border:1px solid var(--pink);color:var(--pink);font-size:11px;border-radius:2px;background:#fff}
.pickup-form .btn-outline{position:absolute;right:24px;bottom:22px}

/* welcome */
.welcome{position:absolute;left:0;top:720px;width:1200px;text-align:center}
.welcome h2{font-size:30px;font-weight:400;color:var(--ink)}
.welcome p{width:500px;margin:26px auto 0;font-size:11px;line-height:1.65;color:var(--muted)}
.welcome .btn-outline{margin-top:26px}

/* features */
.features{position:absolute;left:0;top:1010px;width:1200px;height:620px;background:var(--grey-bg)}
.features h2{position:absolute;top:38px;width:100%;text-align:center;font-size:25px;font-weight:400}
.features .sub{position:absolute;top:76px;width:100%;text-align:center;font-size:11px;color:var(--muted)}
.hub{position:absolute;left:420px;top:182px;width:360px;height:360px;border-radius:50%;background:#fff;box-shadow:0 0 0 1px var(--line)}
.hub-name{position:absolute;left:420px;top:340px;width:360px;text-align:center;font-size:34px;font-weight:400;color:var(--ink)}
.dot{position:absolute;width:8px;height:8px;border-radius:50%;background:#7c7fd6}
.feature{position:absolute;width:260px;display:flex;align-items:center;gap:14px}
.feature.right{flex-direction:row-reverse;text-align:right}
.feature h4{font-size:15px;font-weight:500;color:var(--ink)}
.feature p{font-size:10px;color:var(--muted);margin-top:4px;line-height:1.4}
.icon{flex:none;width:52px;height:40px}

/* faq */
.faq{position:absolute;left:0;top:1640px;width:1200px;height:540px;background:linear-gradient(160deg,var(--teal) 0%,#4cc8d4 60%,var(--teal-dark) 100%)}
.faq h2{position:absolute;top:110px;width:100%;text-align:center;font-size:28px;font-weight:400;color:#fff}
.faq-rule{position:absolute;left:560px;top:152px;width:80px;height:2px;background:rgba(255,255,255,.7)}
.faq-item{position:absolute;width:504px;background:#fff;font-size:11px;color:var(--ink);padding:13px 16px 13px 34px;min-height:40px}
.faq-item::before{content:"+";position:absolute;left:14px;top:10px;font-size:15px;color:var(--teal-dark);font-weight:500}
.faq-item .answer{margin-top:10px;color:var(--muted);line-height:1.5}

/* footer */
.site-footer{position:absolute;left:0;top:2180px;width:1200px;height:268px;background:var(--footer)}
.footer-brand{position:absolute;top:72px;width:100%;text-align:center;font-size:30px;color:#fff;font-weight:400}
.footer-nav{position:absolute;top:128px;width:100%;display:flex;justify-content:center;gap:30px}
.footer-nav a{font-size:11px;color:#c9ccd2;text-decoration:none;font-weight:500}
.footer-nav a.active{color:var(--teal)}
.footer-bottom{position:absolute;left:0;top:202px;width:1200px;height:66px;background:var(--footer-deep);border-top:1px solid #3c414c;text-align:center;font-size:10px;color:#9ba0a8;padding-top:28px}
</style>
</head>
<body>

<header class="site-header">
  <div class="brand">Orvella Aid Fund</div>
  <nav class="main-nav">
    <a class="active" href="#">Home</a>
    <a href="#">About us</a>
    <a href="#">Get Started</a>
    <a href="#">Contact us</a>
  </nav>
  <div class="call">
    <svg width="26" height="26" viewBox="0 0 26 26"><circle cx="13" cy="13" r="12" fill="none" stroke="#cfd2d6"/><path d="M9 8c1-1 2 0 2.5 1.2l.6 1.4c.2.6-.3 1-.7 1.3.6 1.3 1.5 2.2 2.8 2.8.3-.4.7-.9 1.3-.7l1.4.6c1.2.5 2.2 1.5 1.2 2.5-2.2 2.2-10.2-4.9-9.1-9.1z" fill="var(--teal)"/></svg>
    <div class="call-text">Call us<strong>+1 234 567 8907</strong></div>
  </div>
  <div class="btn-green">Donate Now</div>
</header>

<section class="hero" role="img" aria-label="Photo of a father carrying his child on his shoulders at the beach">
  <div class="hero-shade"></div>
  <h1 class="hero-title"><span class="s1">Donate Boat to</span><span class="s2">Charity</span></h1>
  <p class="hero-sub">Your boat can make a difference</p>
</section>

<form class="pickup-form">
  <h3>Donation Pick Up Form</h3>
  <div class="form-label">CONTACT INFORMATION</div>
  <div class="row"><div class="field">First name</div><div class="field">Last name</div></div>
  <div class="row"><div class="field">Zip code</div><div class="field">City phone</div></div>
  <div class="row"><div class="field">Email address</div></div>
  <div class="form-sep"></div>
  <div class="form-label">BOAT DONATION INFORMATION</div>
  <div class="row"><div class="field select">Choose year</div><div class="field select">Choose make</div></div>
  <div class="row"><div class="field">Model of boat</div></div>
  <span class="btn-outline">Submit Application
    <svg width="10" height="8" viewBox="0 0 10 8"><path d="M0 4h9M6 1l3 3-3 3" stroke="currentColor" fill="none"/></svg></span>
</form>

<section class="welcome">
  <h2>Welcome to OAF</h2>
  <p>OAF Foundation's mission is to support, empower and bring hope into the lives of children and their families affected by cancer. OAF helps meet each child's needs, from education to assistance with treatment, recovery and family support.</p>
  <span class="btn-outline">Donate Now
    <svg width="10" height="8" viewBox="0 0 10 8"><path d="M0 4h9M6 1l3 3-3 3" stroke="currentColor" fill="none"/></svg></span>
</section>

<section class="features">
  <h2>Donate Boat to Charity</h2>
  <p class="sub">Your boat can make a difference!</p>

  <div class="hub"></div>
  <div class="hub-name">Orvella Aid Fund</div>
  <span class="dot" style="left:476px;top:220px"></span>
  <span class="dot" style="left:716px;top:220px"></span>
  <span class="dot" style="left:396px;top:358px"></span>
  <span class="dot" style="left:796px;top:358px"></span>
  <span class="dot" style="left:476px;top:496px"></span>
  <span class="dot" style="left:716px;top:496px"></span>

  <div class="feature" style="left:82px;top:218px">
    <svg class="icon" viewBox="0 0 52 40"><path d="M4 26h26v-8h8l6 8v6H4z" fill="none" stroke="#b7bac0" stroke-width="2"/><circle cx="14" cy="33" r="4" fill="#fff" stroke="#b7bac0" stroke-width="2"/><circle cx="38" cy="33" r="4" fill="#fff" stroke="#b7bac0" stroke-width="2"/></svg>
    <div><h4>Free Towing</h4><p>Free Towing On All Boats</p></div>
  </div>
  <div class="feature" style="left:82px;top:350px">
    <svg class="icon" viewBox="0 0 52 40"><path d="M4 24h44l-6 10H10z" fill="var(--teal)"/><path d="M24 22V6l12 16z" fill="var(--teal)" opacity=".7"/></svg>
    <div><h4>All boats</h4><p>We accept All boats</p></div>
  </div>
  <div class="feature" style="left:82px;top:482px">
    <svg class="icon" viewBox="0 0 52 40"><circle cx="26" cy="20" r="15" fill="none" stroke="#b7bac0" stroke-width="2"/><path d="M26 11v9l6 4" stroke="#b7bac0" stroke-width="2" fill="none"/></svg>
    <div><h4>Largest Auction</h4><p>Boat Will Be Sold on the Largest Auction Network</p></div>
  </div>

  <div class="feature right" style="left:858px;top:218px">
    <svg class="icon" viewBox="0 0 52 40"><path d="M8 30l10-10 8 6 14-16" stroke="#b7bac0" stroke-width="2" fill="none"/><path d="M34 10h6v6" stroke="#b7bac0" stroke-width="2" fill="none"/></svg>
    <div><h4>Help Fund</h4><p>Boat Donation Help Fund Charitable Programs</p></div>
  </div>
  <div class="feature right" style="left:858px;top:350px">
    <svg class="icon" viewBox="0 0 52 40"><path d="M26 34C12 24 8 18 8 13a8 8 0 0 1 18-3 8 8 0 0 1 18 3c0 5-4 11-18 21z" fill="#d8dadf"/></svg>
    <div><h4>Hassle Free</h4><p>Hassle Free Donation</p></div>
  </div>
  <div class="feature right" style="left:858px;top:482px">
    <svg class="icon" viewBox="0 0 52 40"><circle cx="26" cy="20" r="15" fill="var(--pink)"/><path d="M20 20l4 4 8-8" stroke="#fff" stroke-width="2.5" fill="none"/></svg>
    <div><h4>Income tax</h4><p>Income Tax Deduction</p></div>
  </div>
</section>

<section class="faq" role="img" aria-label="Soft teal background photo">
  <h2>Frequently Asked Questions</h2>
  <div class="faq-rule"></div>
  <div class="faq-item" style="left:88px;top:200px">What types of boats can be donated?</div>
  <div class="faq-item" style="left:88px;top:258px">What paperwork do I need to donate my boat?</div>
  <div class="faq-item" style="left:88px;top:316px">Is my donated boat tax deductible?</div>
  <div class="faq-item" style="left:88px;top:374px">What if the boat is not registered in my name?</div>
  <div class="faq-item" style="left:608px;top:200px">How much will I receive as a tax deduction for my boat?</div>
  <div class="faq-item" style="left:608px;top:258px">When will I receive my tax receipt?</div>
  <div class="faq-item" style="left:608px;top:316px">How do I schedule a pick up?
    <div class="answer">Please call our toll free number when you are ready to donate<br>1-234-567-8907</div></div>
</section>

<footer class="site-footer">
  <div class="footer-brand">Orvella Aid Fund</div>
  <nav class="footer-nav">
    <a class="active" href="#">HOME</a>
    <a href="#">ABOUT US</a>
    <a href="#">GET STARTED</a>
    <a href="#">CONTACT US</a>
  </nav>
  <div class="footer-bottom">Copyright 2017 Company name Foundation - All Rights Reserved.</div>
</footer>

</body>
</html>
```